Velvet Dune is a premium Spa and Salon only professional tanning brand.

We need a email template/newsletter that we can send to our client base any time we would like to share information with them.
Whether this is launching our Christmas gift, or sharing up and coming training dates it will be another avenue for us to stay in touch with our clients.
We like to think ourselves as the 'Marchetti handbag' in the tanning world, Velvet Dune is a brand that is desirable and exclusive and has people hooked once they trial the brand and are blown away by the results.
www.velvet-dune.com

```html
<!DOCTYPE html>
<html lang="en">
<head>
<meta charset="utf-8">
<title>Velvet Dune – October Newsletter</title>
<link href="https://fonts.googleapis.com/css2?family=Open+Sans:wght@400;600;700&display=swap" rel="stylesheet">
<style>
  :root {
    --page-bg: #fff6ec;
    --card-bg: #ffffff;
    --brand-brown: #8b5a3c;
    --brand-maroon: #7a2c2a;
    --button-red: #762012;
    --text-body: #555555;
    --text-muted: #888888;
    --rule: #dddddd;
    --hero-grey: #ececec;
  }
  * { box-sizing: border-box; margin: 0; padding: 0; }
  html, body {
    width: 740px; height: 1200px; overflow: hidden;
    background: var(--page-bg);
    font-family: "Open Sans", Arial, sans-serif;
  }
  .newsletter {
    position: absolute; left: 92px; top: 28px;
    width: 556px; height: 1145px;
    background: var(--card-bg);
  }
  .header-wordmark {
    position: absolute; left: 19px; top: 56px;
    font-size: 27px; font-weight: 600; color: var(--brand-maroon);
    letter-spacing: 0.5px;
  }
  .issue-date {
    position: absolute; right: 19px; top: 65px;
    font-size: 13px; color: var(--text-muted);
  }
  .hero-band {
    position: absolute; left: 0; top: 150px; width: 556px; height: 370px;
    background: var(--hero-grey);
  }
  .hero-band-tint {
    position: absolute; left: 0; top: 0; width: 300px; height: 132px;
    background: #fbf6f1;
  }
  .hero-photo {
    position: absolute; right: 0; top: 0; width: 280px; height: 370px;
    background: radial-gradient(ellipse at 45% 55%, #c99674 0%, #d9b89b 30%, #e8e2dc 60%, #eeeeee 100%);
  }
  .feature-box {
    position: absolute; left: 19px; top: 140px; width: 278px; height: 389px;
    background: var(--card-bg);
    border: 3px solid var(--brand-brown);
  }
  .feature-image {
    position: absolute; left: 6px; top: 6px; width: 194px; height: 166px;
    background: linear-gradient(135deg, #c79a74 0%, #dcccb8 45%, #e3d6c6 100%);
  }
  .feature-title {
    position: absolute; left: 6px; top: 180px; width: 255px;
    font-size: 18.5px; line-height: 22px; font-weight: 400; color: var(--brand-maroon);
  }
  .feature-text {
    position: absolute; left: 6px; top: 248px; width: 258px;
    font-size: 13px; line-height: 19.5px; color: var(--text-body);
  }
  .read-more {
    position: absolute; left: 79px; top: 505px; width: 137px; height: 45px;
    background: var(--card-bg); border: 2px solid #222;
    font-size: 13px; letter-spacing: 0.5px; color: #222;
    display: flex; align-items: center; justify-content: center;
  }
  .story-image {
    position: absolute; left: 0; top: 596px; width: 222px; height: 313px;
    background: linear-gradient(90deg, #d6b596 0%, #e6d8c8 55%, #ffffff 100%);
  }
  .story-title {
    position: absolute; left: 160px; top: 672px; width: 380px;
    font-size: 40px; line-height: 47px; font-weight: 400;
    letter-spacing: 1.5px; color: var(--brand-brown);
  }
  .story-text {
    position: absolute; left: 160px; top: 774px; width: 385px;
    font-size: 13.5px; line-height: 19.5px; letter-spacing: 0.3px; color: var(--text-body);
  }
  .story-text strong { font-weight: 700; color: #444; }
  .link-buttons {
    position: absolute; left: 59px; top: 894px; display: flex; gap: 12px;
  }
  .link-button {
    width: 139px; height: 31px; background: var(--button-red); color: #fff;
    font-size: 13.5px; display: flex; align-items: center; justify-content: center;
  }
  .footer-rule {
    position: absolute; left: 19px; top: 972px; width: 518px; height: 1px; background: var(--rule);
  }
  .footer-contact {
    position: absolute; left: 19px; top: 1015px;
    font-size: 11.5px; line-height: 16.5px; color: #444;
  }
  .footer-name { font-size: 17px; line-height: 22px; color: var(--brand-brown); }
  .footer-email { color: #444; text-decoration: underline; }
  .footer-badges { position: absolute; left: 369px; top: 1030px; display: flex; gap: 36px; }
</style>
</head>
<body>
  <main class="newsletter">
    <header>
      <div class="header-wordmark">Velvet Dune</div>
      <div class="issue-date">October 2014</div>
    </header>

    <section class="hero-band">
      <div class="hero-band-tint"></div>
      <div class="hero-photo" role="img" aria-label="Photo of a woman seated with a towel, seen from behind, with autumn leaves swirling around her shoulder"></div>
    </section>

    <article class="feature-box">
      <div class="feature-image" role="img" aria-label="Product advert showing tanned legs with autumn leaves and the Velvet Dune name"></div>
      <h2 class="feature-title">Great news! The 2-6 hour tanning revolution has ar­rived</h2>
      <p class="feature-text">This revolutionary new rapid tanning product takes just 2-6 hours to develop, and allows you to control the depth of your tan by choosing for yourself when to shower it off.</p>
    </article>
    <div class="read-more">READ MORE</div>

    <section>
      <div class="story-image" role="img" aria-label="Photo of tanned legs surrounded by falling autumn leaves"></div>
      <h1 class="story-title">A revolution in self tanning</h1>
      <p class="story-text">Developed with a unique <strong>organic formula</strong>, enriched with deep moisturisers and free from <strong>paraben</strong> and <strong>alcohol</strong>, ensuring a streak-free, soft finish.</p>
      <nav class="link-buttons">
        <div class="link-button">Browse products</div>
        <div class="link-button">Expert tips</div>
        <div class="link-button">Find a stockist</div>
      </nav>
    </section>

    <div class="footer-rule"></div>
    <footer>
      <div class="footer-contact">
        <div class="footer-name">Velvet Dune</div>
        <div class="footer-email">hello@velvet-dune.com</div>
        <div>Harrowfield Business Centre</div>
        <div>Mill Lane Trading Park</div>
        <div>Dunmore, County Antrim BT41 7XZ</div>
      </div>
      <div class="footer-badges">
        <svg width="56" height="56" viewBox="0 0 56 56" role="img" aria-label="Cruelty-free certification badge"><rect x="6" y="6" width="44" height="44" rx="6" fill="none" stroke="#9a5a34" stroke-width="3"/></svg>
        <svg width="56" height="56" viewBox="0 0 56 56" role="img" aria-label="Organic certification badge"><circle cx="28" cy="28" r="26" fill="#9a5a34"/></svg>
      </div>
    </footer>
  </main>
</body>
</html>
```